Mr. Kelpie Restaurant Menu Design

I would like for you to please create a menu design for my seafood restaurant called Mr. Kelpie. I uploaded the logo of my restaurant and would like the same colors and font to be used on the menu. The headings of my menu should include the following:
What's your catch?
What's your sauce?
How "Hot" can you go?
Medium?
Mild?
Wild?
Soups
Paella
Katsu
Add Ons
Sweet Cravings
Thirsty?
It would be nice to see something creative and simple preferably one page.
I already uploaded my logo on the brief section.
Thank you.
Target Market(s)
Family friendly
Industry/Entity Type
Seafood Restaurant
Look and feel

```html
<!DOCTYPE html>
<html lang="en">
<head>
<meta charset="utf-8">
<title>Mr. Kelpie Restaurant Menu</title>
<link rel="stylesheet" href="https://fonts.googleapis.com/css2?family=Open+Sans:wght@400;700&display=swap">
<style>
  :root {
    --orange: #e8791b;
    --orange-deep: #d9650a;
    --orange-text: #e07a12;
    --ink: #1e1e1e;
    --white: #ffffff;
  }
  * { margin: 0; padding: 0; box-sizing: border-box; }
  html, body { width: 927px; height: 1200px; overflow: hidden; background: var(--white); }
  body { font-family: "Open Sans", Arial, sans-serif; }
  .menu-page { position: relative; width: 927px; height: 1200px; overflow: hidden; background: var(--white); }

  .header-band { position: absolute; left: 0; top: 0; width: 927px; height: 700px; }

  .brand-name {
    position: absolute; left: 50px; top: 160px; width: 290px; text-align: center;
    font-weight: 400; font-size: 48px; line-height: 1; color: var(--white);
  }

  .platter-photo {
    position: absolute; left: 468px; top: 14px; width: 572px; height: 572px; border-radius: 50%;
    background: radial-gradient(circle at 62% 58%, #c7361c 0%, #d9542f 22%, #f0c3a8 48%, #b2334f 70%, #8a7a4a 100%);
  }

  .headline {
    position: absolute; left: 48px; top: 470px;
    font-size: 70px; font-weight: 400; line-height: 73px; color: var(--orange-text); letter-spacing: 2px;
    white-space: nowrap;
  }

  .section-list { position: absolute; left: 62px; top: 657px; list-style: none; }
  .section-list li {
    display: flex; align-items: center; height: 54.5px;
    font-size: 29px; color: var(--ink);
  }
  .section-list li::before {
    content: ""; width: 0; height: 0; margin-right: 12px;
    border-top: 7px solid transparent; border-bottom: 7px solid transparent; border-left: 8px solid var(--ink);
  }

  .prawn-photo {
    position: absolute; left: 482px; top: 800px; width: 520px; height: 470px;
    border-radius: 46% 20% 0 50% / 50% 30% 0 50%;
    background: radial-gradient(ellipse at 45% 55%, #e0603a 0%, #c9432a 40%, #f0d5b8 70%, #5a4d44 100%);
  }
</style>
</head>
<body>
<main class="menu-page">
  <svg class="header-band" viewBox="0 0 927 700" aria-hidden="true">
    <defs>
      <linearGradient id="bandFill" x1="0" y1="0" x2="0" y2="1">
        <stop offset="0" stop-color="#d9650a"/>
        <stop offset="1" stop-color="#e8791b"/>
      </linearGradient>
    </defs>
    <path d="M0 0 H927 V360 H520 C400 355 200 380 0 482 Z" fill="url(#bandFill)"/>
    <circle cx="755" cy="300" r="329" fill="#e8791b"/>
  </svg>

  <p class="brand-name">Mr. Kelpie</p>

  <div class="platter-photo" role="img" aria-label="Photo of a seafood platter with lobster, shrimp and a bowl of red cocktail sauce"></div>

  <h1 class="headline">How "Hot"<br>Can You Go?</h1>

  <ul class="section-list">
    <li>Medium?</li>
    <li>Mild?</li>
    <li>Wild?</li>
    <li>Soups</li>
    <li>Paella</li>
    <li>Katsu</li>
    <li>Add Ons</li>
    <li>Sweet Cravings</li>
    <li>Thirsty?</li>
  </ul>

  <div class="prawn-photo" role="img" aria-label="Photo of grilled prawns and lobster tails on a plate"></div>
</main>
</body>
</html>
```